Business card design and logo needed

We have been operating as Ridgeline Paddock Fencing for 30 years but never had a logo and feel there is a need for one, but have no idea for a design.
We specialise in all types of rural fencing including post and wire, post and rail, electric, chainmesh and to a lesser extent, also do industrial security fencing.
Updates

Sorry, but website is ridgelinepaddock.net

No .au on the end!
My apologies

Regards, Barry

Target Market(s)

Rural/acreage property owners, particularly horse people.

Industry/Entity Type

Industrial

Contact Information for Business Card

Ridgeline Paddock Fencing Barry Lindqvist 0427 615302. Terry Lindqvist 0427 783160
Email: ridgelinepaddock@quolmail.com.au
Website: www.ridgelinepaddock.net.au

Requirements
Must have
• Would like to highlight website address - use the business card to advertise the website or to push them to check it out.

```html
<!DOCTYPE html>
<html lang="en">
<head>
<meta charset="utf-8">
<title>Ridgeline Paddock Fencing – Business Card</title>
<link href="https://fonts.googleapis.com/css2?family=Arimo:wght@400&display=swap" rel="stylesheet">
<style>
  :root {
    --ink: #1b1b1b;
    --rule: #8a8a8a;
    --wash-light: #f1f1f0;
    --wash-mid: #dcdcdb;
    --wash-dark: #c9c9c8;
  }
  * { margin: 0; padding: 0; box-sizing: border-box; }
  html, body {
    width: 686px;
    height: 1200px;
    overflow: hidden;
    background: var(--wash-light);
  }
  .card {
    position: relative;
    width: 686px;
    height: 1200px;
    overflow: hidden;
    font-family: "Arimo", Arial, sans-serif;
    color: var(--ink);
  }
  .card__texture {
    position: absolute;
    inset: 0;
    background: linear-gradient(170deg, var(--wash-light) 0%, var(--wash-mid) 45%, var(--wash-light) 70%, var(--wash-dark) 100%);
  }
  .brand {
    position: absolute;
    left: 79px;
    top: 76px;
    width: 346px;
    height: 346px;
  }
  .brand__ring {
    position: absolute;
    inset: 0;
  }
  .brand__name {
    position: absolute;
    inset: 0;
    display: flex;
    align-items: center;
    justify-content: center;
    text-align: center;
    padding: 0 60px;
    font-size: 34px;
    line-height: 1.25;
    color: var(--ink);
  }
  .contact {
    position: absolute;
    left: 132px;
    top: 826px;
    width: 441px;
  }
  .contact__company {
    font-size: 27px;
    line-height: 36px;
    margin-bottom: 12px;
  }
  .contact__line {
    font-size: 28px;
    line-height: 41px;
  }
  .contact__email {
    font-size: 27px;
    line-height: 40px;
  }
  .contact__web {
    margin-top: 45px;
    border-top: 1.5px solid var(--rule);
    border-bottom: 1.5px solid var(--rule);
    padding: 10px 0 11px;
    font-size: 29px;
    line-height: 32px;
  }
</style>
</head>
<body>
  <div class="card">
    <div class="card__texture" role="img" aria-label="Whitewashed timber board texture in soft greys"></div>

    <div class="brand">
      <svg class="brand__ring" viewBox="0 0 346 346" aria-hidden="true">
        <circle cx="173" cy="173" r="170" fill="none" stroke="var(--ink)" stroke-width="3"/>
      </svg>
      <div class="brand__name">Ridgeline Paddock Fencing</div>
    </div>

    <div class="contact">
      <p class="contact__company">Ridgeline Paddock Fencing</p>
      <p class="contact__line">Barry Lindqvist 0427 615302</p>
      <p class="contact__line">Terry Lindqvist 0427 783160</p>
      <p class="contact__email">ridgelinepaddock@quolmail.com.au</p>
      <p class="contact__web">www.ridgelinepaddock.net</p>
    </div>
  </div>
</body>
</html>
```